Thornwell Building Company - advertisement poster

I am looking to print some canvas signs to advertise my general contracting company, Thornwell Building Company. The sign will measure 6' long x 3' high so the size should match that ratio. I already have a logo icon, which is the Letter 'A' and some trees that I would like to incorporate, see attached. I would also like the to have the following information listed:
1) phone number: 472-318-6095
2) email: thornwellbuildingcompany@mailvistra.net
3) website: thornwellbuildingcompany.com
4) Lic#5386204
5) I want to use this text: "BUILD WITH THE T-CREW!"

The ad should be relatively simple and clean. Black and Green are my company colors. I am open to creative ideas!

Target Market(s)

People looking to renovate their homes

Industry/Entity Type

Construction

Colors
59FF00
82FF00
B8FF75
E3FFCB
F4FFEA

Requirements
Must have
• Must have my company logo
Should not have
• No photos or complex graphics

```html
<!DOCTYPE html>
<html lang="en">
<head>
<meta charset="utf-8">
<title>Thornwell Building Company – Build With The T-Crew!</title>
<link href="https://fonts.googleapis.com/css2?family=Montserrat:wght@500;600;700;800&family=Oswald:wght@600&family=Kaushan+Script&display=swap" rel="stylesheet">
<style>
  :root {
    --green: #6ab344;
    --black: #0b0b0b;
    --stripe-dark: #1a1a1a;
    --white: #ffffff;
    --ghost: #ebebeb;
    --skyline: #1f3a14;
  }
  * { margin: 0; padding: 0; box-sizing: border-box; }
  html, body { width: 1200px; height: 600px; overflow: hidden; background: var(--white); }
  .poster {
    position: relative;
    width: 1200px;
    height: 600px;
    overflow: hidden;
    background: var(--white);
    font-family: "Montserrat", Arial, sans-serif;
  }
  .city-sketch {
    position: absolute;
    left: 0; top: 200px;
    width: 400px; height: 400px;
    background: linear-gradient(180deg, rgba(235,235,235,0) 0%, var(--ghost) 45%, #e2e2e2 100%);
    clip-path: polygon(0 0, 100% 0, 71% 100%, 0 100%);
  }
  .backdrop { position: absolute; inset: 0; }
  .skyline-glow {
    position: absolute;
    left: 380px; top: 527px;
    width: 820px; height: 73px;
    background: linear-gradient(180deg, rgba(31,58,20,0) 0%, var(--skyline) 100%);
    clip-path: polygon(3% 0, 100% 0, 100% 100%, 0 100%);
  }
  .brand {
    position: absolute;
    left: 40px; top: 60px;
    width: 340px;
    text-align: center;
    color: var(--black);
  }
  .brand-mark {
    width: 84px; height: 84px;
    margin: 0 auto;
    background: var(--green);
  }
  .brand-est {
    position: absolute;
    left: 20px; right: 20px; top: 60px;
    display: flex;
    justify-content: space-between;
    font-size: 12px;
    font-weight: 600;
    letter-spacing: 3px;
  }
  .brand-name {
    margin-top: 10px;
    font-size: 44px;
    font-weight: 800;
    line-height: 1;
    letter-spacing: 1px;
    text-transform: uppercase;
  }
  .brand-name small {
    display: block;
    font-size: 18px;
    font-weight: 600;
    letter-spacing: 5px;
    margin-top: 8px;
  }
  .headline {
    position: absolute;
    left: 590px; top: 58px;
    width: 570px;
    text-align: center;
  }
  .headline-script {
    display: block;
    font-family: "Kaushan Script", cursive;
    font-size: 80px;
    line-height: 1;
    color: var(--white);
  }
  .headline-bold {
    display: block;
    font-family: "Oswald", Arial, sans-serif;
    font-weight: 600;
    font-size: 78px;
    line-height: 1.05;
    letter-spacing: 7px;
    color: var(--green);
  }
  .contact {
    position: absolute;
    left: 493px; top: 467px;
    width: 580px; height: 64px;
    background: var(--white);
    display: grid;
    grid-template-columns: 138px 1fr;
    align-content: center;
    row-gap: 8px;
    padding: 0 12px 0 30px;
    font-size: 13px;
    font-weight: 700;
    color: var(--black);
  }
  .contact-item { display: flex; align-items: center; gap: 9px; white-space: nowrap; }
  .contact-item svg { width: 16px; height: 16px; flex: none; fill: var(--black); }
</style>
</head>
<body>
<main class="poster">
  <div class="city-sketch" role="img" aria-label="Faint grey skyline with construction cranes"></div>

  <svg class="backdrop" viewBox="0 0 1200 600" width="1200" height="600" aria-hidden="true">
    <defs>
      <pattern id="hazard" width="44" height="44" patternUnits="userSpaceOnUse" patternTransform="rotate(-32)">
        <rect width="44" height="44" fill="#1a1a1a"/>
        <rect width="26" height="44" fill="#6ab344"/>
      </pattern>
    </defs>
    <polygon points="587,0 1200,0 1200,600 357,600" fill="#0b0b0b"/>
    <polygon points="517,0 587,0 357,600 284,600" fill="url(#hazard)"/>
  </svg>

  <div class="skyline-glow" role="img" aria-label="Green line-drawn city skyline along the bottom edge"></div>

  <div class="brand">
    <div class="brand-mark"></div>
    <div class="brand-est"><span>ESTD</span><span>2020</span></div>
    <h1 class="brand-name">Thornwell<small>Building Company</small></h1>
  </div>

  <h2 class="headline">
    <span class="headline-script">Build With</span>
    <span class="headline-bold">The T-Crew!</span>
  </h2>

  <section class="contact" aria-label="Contact details">
    <div class="contact-item">
      <svg viewBox="0 0 24 24"><path d="M6.6 10.8a15.1 15.1 0 0 0 6.6 6.6l2.2-2.2c.3-.3.7-.4 1-.2 1.1.4 2.3.6 3.6.6.6 0 1 .4 1 1V20c0 .6-.4 1-1 1A17 17 0 0 1 3 4c0-.6.4-1 1-1h3.5c.6 0 1 .4 1 1 0 1.3.2 2.5.6 3.6.1.3 0 .7-.2 1z"/></svg>
      <span>472-318-6095</span>
    </div>
    <div class="contact-item">
      <svg viewBox="0 0 24 24"><path d="M12 2a10 10 0 1 0 0 20 10 10 0 0 0 0-20zm6.9 6h-2.9a15.6 15.6 0 0 0-1.4-3.6A8 8 0 0 1 18.9 8zM12 4c.8 1.2 1.5 2.5 1.9 4h-3.8c.4-1.5 1.1-2.8 1.9-4zM4.3 14a8 8 0 0 1 0-4h3.4a16.5 16.5 0 0 0 0 4zm.8 2h2.9c.3 1.3.8 2.5 1.4 3.6A8 8 0 0 1 5.1 16zM8 8H5.1a8 8 0 0 1 4.3-3.6C8.8 5.5 8.3 6.7 8 8zm4 12c-.8-1.2-1.5-2.5-1.9-4h3.8c-.4 1.5-1.1 2.8-1.9 4zm2.3-6H9.7a14.7 14.7 0 0 1 0-4h4.6a14.7 14.7 0 0 1 0 4zm.3 5.6c.6-1.1 1.1-2.3 1.4-3.6h2.9a8 8 0 0 1-4.3 3.6zm1.7-5.6a16.5 16.5 0 0 0 0-4h3.4a8 8 0 0 1 0 4z"/></svg>
      <span>website: thornwellbuildingcompany.com</span>
    </div>
    <div class="contact-item">
      <span>Lic#5386204</span>
    </div>
    <div class="contact-item">
      <svg viewBox="0 0 24 24"><path d="M2 5h20v14H2zm2 2v.5l8 5.5 8-5.5V7zm0 2.9V17h16V9.9l-8 5.5z"/></svg>
      <span>email: thornwellbuildingcompany@mailvistra.net</span>
    </div>
  </section>
</main>
</body>
</html>
```